Pack - Adventurous, Fun, Exciting, Social Fitness Club needs a Webpage with attitude!

Pack... we're a fun, social, outdoor fitness club that needs not just a homepage designed for our website, but in the process a "personality" for our unique, innovative and cheeky brand.
We pride ourselves on getting our members outdoors trying new, exciting physical activities in an effort to find joy in an active lifestyle, and sharing that experience with other like minded people. We offer:
- Personal Training (1-on-1 Fitness Training)
- Group Fitness Classes (Boxing, Pilates, etc)
- Boot Camps (Military Style - Sandbags, Ropes, Tyres, etc)
- Events (Fun Runs, Triathlons, Ocean Swims, Treks, etc)
- Adventures(Quorra Ridge Trek, Rock Climbing, Kayaking, etc)
Our tag line is 'No Judgements. No Limits!' The homepage should be exciting, adventurous and innovative, illustrating the values of our brand: possibility, thirst for life, personal accomplishment & freedom. It should be fun, friendly & inviting.
A few of our key benefits to members are:
- No Boring Workouts
- No Joining Fees or Long Term Contracts
- Results Guaranteed
The links below should give you a rough idea of the sort of "feel" we're after (vibrant, active, adventurous ).
http://www.campusroamer.com.au/
http://www.layoutgoblin.com/website-templates/31924.html
http://www.layoutgoblin.com/website-templates/32751.html
http://www.velmora.com/
Target Market(s)
Real, Everyday People - Men & Women (30:70) aged mainly between 21-40, who want a more exciting and enjoyable fitness experience than your typical gym offers.
Industry/Entity Type
Fitness
Requirements
Must have
- Strong, uplifting and motivating images of people enjoying fitness/physical activities outdoors

```html
<!DOCTYPE html>
<html lang="en">
<head>
<meta charset="utf-8">
<title>Pack – Outdoor Fitness Club</title>
<link rel="stylesheet" href="https://fonts.googleapis.com/css2?family=Ubuntu:wght@400;500;700&family=Noto+Serif:wght@400&display=swap">
<style>
:root{
  --orange:#e75c09;
  --orange-deep:#e05406;
  --orange-soft:#ee8a4c;
  --yellow:#f8cf06;
  --yellow-nav:#f9d73a;
  --yellow-field:#fbe97a;
  --cream:#fef5d3;
  --red:#d30f16;
  --white:#ffffff;
  --ink:#333333;
  --nav-ink:#7a3a06;
  --blue:#1f73b4;
}
*{box-sizing:border-box;margin:0;padding:0}
html,body{width:1108px;height:1200px;overflow:hidden;background:var(--white)}
body{font-family:"Ubuntu",sans-serif;color:var(--ink)}
.page{position:relative;width:1200px;height:1300px;transform:scale(0.92334);transform-origin:0 0}
.abs{position:absolute}

.scenery{left:0;top:0;width:1200px;height:557px;background:linear-gradient(180deg,#9cc5e6 0%,#cfe2ef 30%,#b8d08a 52%,#6e9b34 70%,#4f7f22 100%)}

.header{left:100px;top:0;width:1000px;height:148px;background:linear-gradient(100deg,#fbc21a 0%,#f49a10 22%,var(--orange) 45%,var(--orange) 100%)}
.brand{left:28px;top:30px;display:flex;align-items:center;gap:12px}
.brand-mark{width:22px;height:22px;border-radius:50%;background:var(--ink)}
.brand-name{font-size:58px;font-weight:700;color:var(--ink);letter-spacing:1px;line-height:1}
.tagline{left:41px;top:121px;font-size:15px;font-weight:500;color:#1a1a1a}
.utility{right:0;top:0;width:332px;height:90px}
.utility-rule{left:0;top:52px;width:332px;height:1px;background:rgba(255,255,255,.7)}
.utility-item{top:10px;display:flex;flex-direction:column;align-items:center;gap:15px;font-size:14px;font-weight:700;color:var(--white)}
.utility-icon{width:34px;height:34px;border-radius:50%;background:var(--white);display:flex;align-items:center;justify-content:center}

.nav{left:100px;top:148px;width:1000px;height:57px;background:linear-gradient(180deg,#fbe052,var(--yellow-nav))}
.nav-links{left:22px;top:24px;display:flex;gap:35px;font-size:16px;color:var(--nav-ink);list-style:none}
.nav-divider{left:701px;top:0;width:1px;height:57px;background:#d9a826}
.call{left:730px;top:19px;font-size:17px;color:var(--nav-ink);display:flex;align-items:baseline;gap:9px}
.call strong{font-size:28px;font-weight:500;color:var(--red)}

.hero{left:100px;top:205px;width:1000px;height:352px;background:var(--orange)}
.slider{left:23px;top:21px;width:622px;height:313px;background:var(--white);box-shadow:0 2px 4px rgba(0,0,0,.3)}
.slide-photo{left:7px;top:6px;width:610px;height:300px;background:linear-gradient(120deg,#6e6a45 0%,#a99a6a 40%,#d8c7ae 60%,#7c2e2a 100%)}
.caption{left:169px;top:206px;width:448px;height:100px;background:rgba(40,40,40,.6);border-left:1px solid rgba(255,255,255,.4);color:var(--white)}
.caption-tags{left:16px;top:8px;display:flex;gap:24px;font-size:27px;align-items:center}
.caption-tags span{display:flex;align-items:center;gap:10px}
.caption-quote{left:16px;top:48px;font-size:14px;font-style:italic}
.caption-by{right:24px;top:72px;font-size:14px;font-style:italic}
.dots{left:15px;top:282px;display:flex;gap:11px}
.dot{width:18px;height:18px;border-radius:50%;background:var(--red)}
.dot.is-active{background:#fbf2d0}

.offer{left:670px;top:25px;width:310px;height:308px;background:var(--white);transform:rotate(.4deg)}
.offer-inner{left:11px;top:8px;width:289px;height:290px;background:var(--yellow)}
.offer-title{left:24px;top:6px;font-family:"Noto Serif",serif;font-size:31px;color:var(--white)}
.offer-value{right:22px;top:43px;font-size:13px;color:var(--white)}
.perks{left:6px;top:68px;width:277px;list-style:none}
.perks li{height:28px;border-top:1px solid #f2b806;display:flex;align-items:center;gap:9px;font-size:14px;color:var(--red);padding-left:6px}
.field{left:21px;font-size:13px;font-weight:700;color:var(--red)}
.field-input{left:73px;width:125px;height:18px;background:var(--yellow-field)}
.join{left:186px;top:256px;width:89px;height:24px;background:var(--red);color:var(--white);font-size:12px;font-weight:700;display:flex;align-items:center;justify-content:center;border:1px solid var(--white)}

.services{left:100px;top:557px;width:1000px;height:353px;background:var(--yellow)}
.card{top:22px;width:303px;height:310px;background:var(--white)}
.card-photo{left:6px;top:6px;width:291px;height:210px}
.card-band{left:6px;top:216px;width:291px;height:89px;background:var(--orange-deep);color:var(--white);text-align:center}
.card-band svg{position:absolute;left:0;top:0}
.card-title{position:absolute;left:50px;right:0;top:14px;font-size:20px;font-weight:700}
.card-text{position:absolute;left:50px;right:0;top:42px;font-size:15px;line-height:20px}

.about{left:102px;top:910px;width:643px;height:290px;background:var(--cream);border-left:1px solid var(--orange)}
.about h1{position:absolute;left:20px;top:33px;font-size:25px;font-weight:400;color:var(--orange)}
.about p{position:absolute;left:20px;width:605px;font-size:13.5px;line-height:18px;text-align:justify;color:var(--ink)}
.media{left:745px;top:910px;width:355px;height:290px;background:var(--orange-soft)}
.player{left:17px;top:12px;width:318px;height:266px;background:var(--blue);border:2px solid #5aa0d6}
.player-view{left:5px;top:5px;width:304px;height:228px;background:linear-gradient(90deg,#5b5b5b,#d8d8dc 45%,#b9a58f 75%,#2e2e2e)}
.play-btn{left:126px;top:96px;width:52px;height:38px;border-radius:6px;background:rgba(140,140,140,.7);border:1px solid rgba(255,255,255,.6)}
.controls{left:5px;top:236px;width:304px;height:20px;background:linear-gradient(#eaeaea,#9c9c9c);font-size:8px;color:#222}

.footer{left:0;top:1200px;width:1200px;height:60px;background:var(--orange)}
.copyright{right:130px;top:19px;font-size:10px;font-weight:700;color:var(--white)}
</style>
</head>
<body>
<div class="page">

  <div class="abs scenery" role="img" aria-label="Sunny meadow under a blue sky with colourful ribbons"></div>

  <header class="abs header">
    <div class="abs brand"><span class="brand-mark"></span><span class="brand-name">Pack</span></div>
    <p class="abs tagline">No Judgements. No Limits!</p>
    <nav class="abs utility">
      <div class="abs utility-rule"></div>
      <a class="abs utility-item" style="left:9px">
        <span class="utility-icon"><svg width="16" height="18" viewBox="0 0 16 18"><rect x="2" y="1" width="12" height="16" rx="1" fill="none" stroke="#d30f16" stroke-width="2"/><rect x="5" y="10" width="5" height="4" fill="#d30f16"/></svg></span>TIMETABLE</a>
      <a class="abs utility-item" style="left:114px">
        <span class="utility-icon"><svg width="18" height="20" viewBox="0 0 18 20"><path d="M5 19V6h8" fill="none" stroke="#d30f16" stroke-width="3"/><path d="M11 2l5 4-5 4z" fill="#d30f16"/></svg></span>CLUB LOCATIONS</a>
      <a class="abs utility-item" style="left:265px">
        <span class="utility-icon"><svg width="16" height="18" viewBox="0 0 16 18"><path d="M4 8V5a4 4 0 0 1 8 0v3" fill="none" stroke="#d30f16" stroke-width="2"/><rect x="2" y="8" width="12" height="9" fill="#d30f16"/></svg></span>LOGIN</a>
    </nav>
  </header>

  <div class="abs nav">
    <ul class="abs nav-links">
      <li>HOME</li><li>ABOUT US</li><li>FITNESS</li><li>EVENTS AND ADVENTURES</li><li>CONTACT US</li>
    </ul>
    <div class="abs nav-divider"></div>
    <p class="abs call">CALL US <strong>1300 555 019</strong></p>
  </div>

  <section class="abs hero">
    <div class="abs slider">
      <div class="abs slide-photo" role="img" aria-label="Women stretching together outdoors in a park"></div>
      <div class="abs caption">
        <div class="abs caption-tags">
          <span><svg width="46" height="14" viewBox="0 0 46 14"><path d="M2 9c6-6 10 4 16 0s10-4 16 0h6" fill="none" stroke="#fff" stroke-width="2.5"/><path d="M38 2l8 6-8 5z" fill="#fff"/></svg>Events</span>
          <span style="font-size:24px"><svg width="36" height="12" viewBox="0 0 36 12"><path d="M2 8c5-5 8 3 13 0s8-3 12 0h3" fill="none" stroke="#fff" stroke-width="2.5"/><path d="M29 2l7 5-7 4z" fill="#fff"/></svg>Fun run</span>
        </div>
        <p class="abs caption-quote">"Packs rocks all its events are well organised and enjoyable" !</p>
        <p class="abs caption-by">-Mara Lindqvist</p>
      </div>
      <div class="abs dots"><span class="dot is-active"></span><span class="dot"></span><span class="dot"></span><span class="dot"></span></div>
    </div>

    <aside class="abs offer">
      <div class="abs offer-inner">
        <h2 class="abs offer-title" style="font-weight:400">Free Membership</h2>
        <p class="abs offer-value">(value $65)</p>
        <ul class="abs perks">
          <li><svg width="10" height="12" viewBox="0 0 10 12"><path d="M2 1l6 5-6 5" fill="none" stroke="#fff" stroke-width="3"/></svg>Monthly e-news hints, tips &amp; advice</li>
          <li><svg width="10" height="12" viewBox="0 0 10 12"><path d="M2 1l6 5-6 5" fill="none" stroke="#fff" stroke-width="3"/></svg>VIP invites events &amp; adventures</li>
          <li><svg width="10" height="12" viewBox="0 0 10 12"><path d="M2 1l6 5-6 5" fill="none" stroke="#fff" stroke-width="3"/></svg>special member only offers</li>
          <li style="border-bottom:1px solid #f2b806"><svg width="10" height="12" viewBox="0 0 10 12"><path d="M2 1l6 5-6 5" fill="none" stroke="#fff" stroke-width="3"/></svg>discounts card to 20+ providers</li>
        </ul>
        <span class="abs field" style="top:199px">NAME</span><span class="abs field-input" style="top:198px"></span>
        <span class="abs field" style="top:229px">EMAIL</span><span class="abs field-input" style="top:226px"></span>
        <span class="abs join">JOIN NOW</span>
      </div>
    </aside>
  </section>

  <section class="abs services">
    <article class="abs card" style="left:23px">
      <div class="abs card-photo" role="img" aria-label="Trainer coaching a woman lifting dumbbells beside a pool" style="background:linear-gradient(135deg,#6b5a3c,#b4a38a 50%,#4c7a8a)"></div>
      <div class="abs card-band">
        <svg width="50" height="89" viewBox="0 0 50 89"><path d="M0 0h6l40 44.5L6 89H0z" fill="#fff"/><path d="M8 40h10V30a3 3 0 0 1 6 0v10h4a3 3 0 0 1 3 3v8c0 5-3 8-8 8h-6c-5 0-9-4-9-9z" fill="#e05406"/></svg>
        <h3 class="card-title">PERSONAL TRAINING</h3>
        <p class="card-text" style="left:0">Free initial consult<br>1 on 1 session (valued $80)</p>
      </div>
    </article>
    <article class="abs card" style="left:348px">
      <div class="abs card-photo" role="img" aria-label="Group fitness class doing floor exercises on mats" style="background:linear-gradient(135deg,#8c8d83,#c9bfae 50%,#3e5d8f)"></div>
      <div class="abs card-band">
        <svg width="50" height="89" viewBox="0 0 50 89"><path d="M0 0h6l40 44.5L6 89H0z" fill="#fff"/><path d="M8 40h10V30a3 3 0 0 1 6 0v10h4a3 3 0 0 1 3 3v8c0 5-3 8-8 8h-6c-5 0-9-4-9-9z" fill="#e05406"/></svg>
        <h3 class="card-title">GROUP FITNESS</h3>
        <p class="card-text">Intro pass $25 for 7 days<br>Unlimited classes</p>
      </div>
    </article>
    <article class="abs card" style="left:675px">
      <div class="abs card-photo" role="img" aria-label="Outdoor boot camp group stretching on the grass" style="background:linear-gradient(135deg,#cfd8e0,#4f7a3a 45%,#9a8a6e)"></div>
      <div class="abs card-band">
        <svg width="50" height="89" viewBox="0 0 50 89"><path d="M0 0h6l40 44.5L6 89H0z" fill="#fff"/><path d="M8 40h10V30a3 3 0 0 1 6 0v10h4a3 3 0 0 1 3 3v8c0 5-3 8-8 8h-6c-5 0-9-4-9-9z" fill="#e05406"/></svg>
        <h3 class="card-title">BOOT CAMP</h3>
        <p class="card-text">Starts soon<br>Limited seats</p>
      </div>
    </article>
  </section>

  <section class="abs about">
    <h1>Personal Trainers in Brisbane</h1>
    <p style="top:82px">If you are exercising and have committed a good chunk of time into your fitness, you want to make sure you get the best returns possible. This is where a personal trainer can help. In personal training sessions you will be pushed to achieve your personal best, meaning that you get the best results, both physically and mentally, from your fitness training.</p>
    <p style="top:172px">For those that are new to exercising, it can be difficult to know where to begin. Having a personal trainer on board will give you the guidance and support that you need. Those that enlist the help of a personal trainer often find that they achieve much better results than those that go it alone, and often in a much shorter space of time.</p>
  </section>

  <aside class="abs media">
    <div class="abs player">
      <div class="abs player-view" role="img" aria-label="Video still of a trainer assisting a man on a gym machine"></div>
      <div class="abs play-btn"><svg width="52" height="38" viewBox="0 0 52 38"><path d="M20 10l14 9-14 9z" fill="#fff"/></svg></div>
      <div class="abs controls">
        <svg width="304" height="20" viewBox="0 0 304 20"><path d="M6 5l8 5-8 5z" fill="#222"/><rect x="22" y="8" width="150" height="4" rx="2" fill="#666"/><circle cx="26" cy="10" r="4" fill="#ddd" stroke="#555"/><text x="188" y="13" font-size="8" font-family="Ubuntu, sans-serif" fill="#222">0:00 / 0:00</text><rect x="234" y="4" width="14" height="12" fill="#888"/><rect x="254" y="4" width="18" height="12" fill="#333"/><rect x="278" y="4" width="20" height="12" fill="#333"/><path d="M283 13l5-5 5 5z" fill="#fff"/></svg>
      </div>
    </div>
  </aside>

  <footer class="abs footer">
    <p class="abs copyright">Copyright 2011 Pack</p>
  </footer>

</div>
</body>
</html>
```